Sticker design for prepared meals

I need 3 separate sticker designs for 3 categories of food - all of prepared meal types.
1. Traditional - needs to reflect traditional food/baking of old days Think rustic old style cooking. Maybe a checked table cloth. Maybe a sketch of someone baking with an oven etc.Needs to include our existing logo and wording "Ferdie's Traditional House Made Meals"
2. Takeaway - needs to reflect choice from popular takeaway cuisines - eg Chinese, Thai, Indian, Japanese. Needs to highlight choice - eg family of 4 can get what they want - not all the same cuisine etc. Words " Every family member gets to choose - top quality house made takeaway"
3. Fine Dining - needs to be classy and premium - eg black background with gold lettering - very pristine' very classy. Words include" Ferdie's Fine Dining at your home"
These will be for 3 separate types of stickers 80mm x 30 mm and I will need all files etc to pass onto the sticker company. Thanks

People interested in buying quality food and busy.

• As per project description

```html
<!DOCTYPE html>
<html lang="en">
<head>
<meta charset="utf-8">
<title>Ferdie's Meal Stickers</title>
<link rel="stylesheet" href="https://fonts.googleapis.com/css2?family=Great+Vibes&family=Crimson+Pro:ital,wght@0,700;1,400&family=Josefin+Slab:wght@600&family=Libre+Baskerville:wght@700&family=Cormorant+Garamond:ital,wght@1,500&display=swap">
<style>
  :root {
    --page: #ffffff;
    --plaid-rose: #e2aaa2;
    --plaid-deep: #cf8e88;
    --ink-grey: #4a4a4a;
    --ribbon: #555555;
    --ornament-grey: #e4e4e4;
    --trellis: #d3d3d3;
    --dot-grey: #d6d6d6;
    --taupe: #c2b59b;
    --soft-grey: #cfcfcf;
    --gold-light: #dccb8e;
    --gold-mid: #bea96f;
    --gold-dark: #a38f58;
    --black: #111111;
  }
  html, body {
    margin: 0;
    padding: 0;
    overflow: hidden;
    background: var(--page);
  }
  .canvas {
    position: relative;
    width: 1200px;
    height: 1000px;
    background: var(--page);
    overflow: hidden;
  }
  .sticker {
    position: absolute;
    left: 255px;
    width: 690px;
    height: 258px;
    display: block;
  }
  .sticker--traditional { top: 61px; }
  .sticker--takeaway { top: 368px; }
  .sticker--fine-dining { top: 677px; }

  .brand-name {
    font-family: "Josefin Slab", serif;
    font-weight: 600;
    font-size: 44px;
    fill: var(--ink-grey);
  }
  .ribbon-text {
    font-family: "Josefin Slab", serif;
    font-weight: 600;
    font-size: 12.5px;
    fill: #ffffff;
    letter-spacing: 0.3px;
  }
  .headline-script {
    font-family: "Great Vibes", cursive;
    font-size: 46px;
    fill: var(--taupe);
  }
  .headline-serif {
    font-family: "Crimson Pro", serif;
    font-weight: 700;
    font-size: 25px;
    fill: var(--taupe);
  }
  .tagline {
    font-family: "Crimson Pro", serif;
    font-style: italic;
    font-size: 18px;
    fill: var(--soft-grey);
  }
  .house-name {
    font-family: "Libre Baskerville", serif;
    font-weight: 700;
    font-size: 14px;
    fill: var(--black);
    letter-spacing: 0.5px;
  }
  .fine-title {
    font-family: "Cormorant Garamond", serif;
    font-style: italic;
    font-weight: 500;
    font-size: 33px;
    fill: var(--black);
  }
</style>
</head>
<body>
<main class="canvas">

  <!-- Traditional sticker -->
  <svg class="sticker sticker--traditional" viewBox="0 0 690 258" aria-label="Ferdie's Traditional House Made Meals sticker">
    <defs>
      <clipPath id="trad-clip"><rect width="690" height="258"/></clipPath>
      <linearGradient id="plaid-tone" x1="0" y1="0" x2="1" y2="1">
        <stop offset="0" stop-color="var(--plaid-rose)"/>
        <stop offset="1" stop-color="var(--plaid-deep)"/>
      </linearGradient>
    </defs>
    <g clip-path="url(#trad-clip)">
      <rect class="tablecloth" width="690" height="258" fill="url(#plaid-tone)" role="img" aria-label="Rose checked tablecloth pattern with hand-lettered word Fresh"/>
      <circle class="label-disc" cx="348" cy="128" r="163" fill="var(--page)"/>
      <text class="brand-name" x="348" y="128" text-anchor="middle">Ferdie's</text>
      <polygon class="ribbon" points="200,162 496,162 488,173.5 496,185 200,185 208,173.5" fill="var(--ribbon)"/>
      <text class="ribbon-text" x="348" y="178" text-anchor="middle">Ferdie's Traditional House Made Meals</text>
      <rect class="flourish" x="310" y="198" width="70" height="18" rx="9" fill="var(--ornament-grey)" role="img" aria-label="Looped line flourish"/>
    </g>
  </svg>

  <!-- Takeaway sticker -->
  <svg class="sticker sticker--takeaway" viewBox="0 0 690 258" aria-label="Top quality house made takeaway sticker">
    <defs>
      <clipPath id="take-clip"><rect width="690" height="258"/></clipPath>
    </defs>
    <g clip-path="url(#take-clip)">
      <rect class="trellis" width="690" height="258" fill="var(--trellis)" role="img" aria-label="Grey Moroccan trellis pattern"/>
      <circle class="label-disc" cx="348" cy="129" r="166" fill="var(--page)"/>
      <circle class="dotted-ring" cx="348" cy="129" r="150" fill="none" stroke="var(--dot-grey)" stroke-width="6" stroke-linecap="round" stroke-dasharray="0 13.6"/>
      <text class="headline-script" x="348" y="85" text-anchor="middle">Top Quality</text>
      <text class="headline-serif" x="348" y="131" text-anchor="middle">House Made Takeaway</text>
      <g class="cutlery-icon" fill="none" stroke="#cccccc" stroke-width="2.4" stroke-linecap="round">
        <line x1="337" y1="150" x2="358" y2="184"/>
        <line x1="333" y1="148" x2="336" y2="156"/>
        <line x1="337" y1="146" x2="339" y2="154"/>
        <line x1="341" y1="145" x2="342" y2="153"/>
        <ellipse cx="359" cy="153" rx="5" ry="7.5" transform="rotate(30 359 153)" fill="#cccccc"/>
        <line x1="356" y1="159" x2="339" y2="184"/>
        <path d="M322 154 q4 10 13 16" />
        <path d="M316 158 q5 11 15 17" />
        <path d="M376 154 q-4 10 -13 16" />
        <path d="M382 158 q-5 11 -15 17" />
      </g>
      <text class="tagline" x="348" y="218" text-anchor="middle">Every family member</text>
      <text class="tagline" x="350" y="245" text-anchor="middle">gets to choose</text>
    </g>
  </svg>

  <!-- Fine dining sticker -->
  <svg class="sticker sticker--fine-dining" viewBox="0 0 690 258" aria-label="Ferdie's Fine Dining at your home sticker">
    <defs>
      <clipPath id="fine-clip"><rect width="690" height="258"/></clipPath>
      <linearGradient id="gold-foil" x1="0" y1="0" x2="1" y2="1">
        <stop offset="0" stop-color="var(--gold-mid)"/>
        <stop offset="0.35" stop-color="var(--gold-light)"/>
        <stop offset="0.65" stop-color="var(--gold-dark)"/>
        <stop offset="1" stop-color="var(--gold-light)"/>
      </linearGradient>
    </defs>
    <g clip-path="url(#fine-clip)">
      <rect class="gold-foil" width="690" height="258" fill="url(#gold-foil)" role="img" aria-label="Crinkled gold foil texture"/>
      <circle class="label-disc" cx="348" cy="129" r="163" fill="var(--page)"/>
      <circle class="seal" cx="348" cy="35" r="26" fill="url(#gold-foil)"/>
      <text class="house-name" x="348" y="91" text-anchor="middle">•  FERDIE'S  •</text>
      <line class="rule" x1="227" y1="101" x2="468" y2="101" stroke="var(--black)" stroke-width="1.6"/>
      <text class="fine-title" x="350" y="139" text-anchor="middle">Fine Dining</text>
      <text class="fine-title" x="348" y="178" text-anchor="middle">At Your Home</text>
      <line class="rule" x1="227" y1="197" x2="468" y2="197" stroke="var(--black)" stroke-width="1.6"/>
      <rect class="flourish" x="303" y="214" width="90" height="16" rx="8" fill="var(--gold-light)" role="img" aria-label="Gold scroll ornament"/>
    </g>
  </svg>

</main>
</body>
</html>
```